BANNER FOR JOB FAIR

I need a graphic for a 33W x 81H retractable banner for a job fair.
The banner should use our branded colors and be attractive to people walking by. Some info to put on it:
Commercial Construction
Specializing in Historic Renovation and Urban Development

Start your career in construction with the creative team of Morlo

Maybe a place for a QR code

The final design should communicate that we are a company that is creative and unique and think outside the box. Fun and innovative.
Focusing on Downtown Jacksonville Florida. (doesn't necessarily need to have this)

```html
<!DOCTYPE html>
<html lang="en">
<head>
<meta charset="utf-8">
<title>Morlo – Job Fair Roll-up Banner</title>
<link rel="stylesheet" href="https://fonts.googleapis.com/css2?family=Roboto+Condensed:wght@800&family=Roboto:wght@300;400;700;900&display=swap">
<style>
  :root {
    --navy: #2c4a6e;
    --gold: #d6a92c;
    --ink: #1b1b1b;
    --soft-ink: #3a3a3a;
    --highlight: #e8eaee;
    --paper: #ffffff;
    --backdrop: #e9e9e7;
  }
  * { margin: 0; padding: 0; box-sizing: border-box; }
  html, body {
    width: 1200px;
    height: 1200px;
    overflow: hidden;
    background: var(--backdrop);
  }
  .banner {
    position: absolute;
    left: 370px;
    top: 68px;
    width: 460px;
    height: 1063px;
    background: var(--paper);
    overflow: hidden;
    font-family: "Roboto", Arial, sans-serif;
    color: var(--ink);
  }
  .banner-shapes {
    position: absolute;
    inset: 0;
    width: 100%;
    height: 100%;
  }
  .brand {
    position: absolute;
    left: 172px;
    top: 60px;
    display: flex;
    align-items: center;
    gap: 12px;
  }
  .brand-mark {
    width: 14px;
    height: 14px;
    background: var(--gold);
  }
  .brand-name {
    font-family: "Roboto", Arial, sans-serif;
    font-weight: 900;
    font-size: 48px;
    letter-spacing: 2px;
    color: var(--navy);
    line-height: 1;
  }
  .headline {
    position: absolute;
    left: 38px;
    top: 192px;
    font-family: "Roboto Condensed", "Arial Narrow", sans-serif;
    font-weight: 800;
    text-transform: uppercase;
  }
  .headline-kicker {
    display: block;
    font-size: 45px;
    line-height: 50px;
    color: var(--gold);
  }
  .headline-main {
    display: block;
    font-size: 100px;
    line-height: 82px;
    color: var(--navy);
    margin-top: 6px;
  }
  .specialty {
    position: absolute;
    left: 38px;
    top: 438px;
    font-size: 25px;
    line-height: 33px;
    font-weight: 300;
    color: var(--soft-ink);
  }
  .specialty strong {
    font-weight: 700;
    color: var(--ink);
  }
  .career-highlight {
    position: absolute;
    left: 167px;
    top: 820px;
    width: 293px;
    height: 34px;
    background: var(--highlight);
  }
  .career-call {
    position: absolute;
    left: 38px;
    top: 814px;
    font-size: 31px;
    line-height: 42px;
    font-weight: 400;
    color: var(--ink);
  }
  .career-call strong { font-weight: 900; }
  .career-call .team { font-weight: 700; color: var(--gold); }
  .location {
    position: absolute;
    left: 0;
    right: 0;
    top: 988px;
    text-align: center;
    font-size: 19px;
    font-weight: 700;
    color: var(--ink);
  }
  .footer-rule {
    position: absolute;
    left: 106px;
    top: 1036px;
    width: 248px;
    height: 7px;
    background: var(--navy);
  }
</style>
</head>
<body>
  <main class="banner">
    <svg class="banner-shapes" viewBox="0 0 290 670" preserveAspectRatio="none" aria-hidden="false">
      <defs>
        <linearGradient id="site-tones" x1="0" y1="0" x2="0.4" y2="1">
          <stop offset="0" stop-color="#b98b5c"/>
          <stop offset="0.45" stop-color="#8c6a4c"/>
          <stop offset="1" stop-color="#6b5a4a"/>
        </linearGradient>
      </defs>
      <polygon class="shape-gold-frame" points="120,495 272,196 422,495" fill="var(--gold)"/>
      <g role="img" aria-label="Photo of two construction workers in hi-vis vests and hard hats in front of scaffolding on a building site">
        <polygon class="shape-site-photo" points="172,468 272,268 372,468" fill="url(#site-tones)"/>
      </g>
      <polygon class="shape-gold-accent" points="282,198 290,198 290,224 278,246 272,236" fill="var(--gold)"/>
      <polygon class="shape-navy-stripe" points="83,495 101,495 160,370 142,370" fill="var(--navy)"/>
    </svg>

    <header class="brand">
      <span class="brand-mark"></span>
      <span class="brand-name">MORLO</span>
    </header>

    <h1 class="headline">
      <span class="headline-kicker">Commercial</span>
      <span class="headline-main">Const<br>ruction</span>
    </h1>

    <p class="specialty">Specializing in Historic<br>Renovation and<br><strong>Urban Development</strong></p>

    <div class="career-highlight"></div>
    <p class="career-call">Start your career<br>in <strong>construction</strong> with<br>the creative <span class="team">team of Morlo</span></p>

    <p class="location">Downtown Jacksonville Florida</p>
    <div class="footer-rule"></div>
  </main>
</body>
</html>
```